we need to wrap a van that will be used as a mobile law office

we need to wrap a van that will be used to market for legal cases

Target Market(s)

we are wrapping a van that will provide legal services

Industry/Entity Type

Legal

Logo Text

The Harbor Rig

Logo styles of interest
Emblem Logo
Font styles to use
Serif

Requirements
Must have
• The Harbor Rig
Injured?
Overtime/Wage and Hour claims
1-800-HAR-BOR7
Mobile Law Office - we come to you
THEHARBORRIG.COM
Nice to have
• we need a nice logo to go with the design

```html
<!DOCTYPE html>
<html lang="en">
<head>
<meta charset="UTF-8">
<title>The Harbor Rig – Mobile Law Office</title>
<link rel="stylesheet" href="https://fonts.googleapis.com/css2?family=Open+Sans:wght@400;700&family=Yellowtail&family=Pathway+Gothic+One&display=swap">
<style>
  :root {
    --bg: #ffffff;
    --brand-red: #e21e2b;
    --ink: #000000;
    --url-grey: #3a3a3c;
  }
  html, body {
    margin: 0;
    padding: 0;
    overflow: hidden;
    background: var(--bg);
  }
  .wrap-panel {
    position: relative;
    width: 1200px;
    height: 939px;
    background: var(--bg);
    overflow: hidden;
  }
  .brand-name {
    position: absolute;
    left: 398px;
    top: 282px;
    margin: 0;
    font-family: "Open Sans", Arial, sans-serif;
    font-weight: 700;
    color: var(--brand-red);
    line-height: 1;
  }
  .brand-name__small {
    display: block;
    font-size: 78px;
    letter-spacing: -1px;
  }
  .brand-name__large {
    display: block;
    margin-top: 6px;
    font-size: 80px;
    letter-spacing: -1px;
  }
  .site-url {
    position: absolute;
    right: 300px;
    top: 452px;
    margin: 0;
    font-family: "Open Sans", Arial, sans-serif;
    font-weight: 400;
    font-size: 42px;
    letter-spacing: 1px;
    color: var(--url-grey);
    line-height: 1;
  }
  .tagline {
    position: absolute;
    left: 0;
    width: 1266px;
    top: 508px;
    margin: 0;
    text-align: center;
    font-family: "Yellowtail", cursive;
    font-size: 60px;
    color: var(--ink);
    line-height: 1.1;
  }
  .practice-area,
  .phone {
    position: absolute;
    left: 0;
    width: 1266px;
    margin: 0;
    text-align: center;
    font-family: "Pathway Gothic One", "Arial Narrow", sans-serif;
    color: var(--ink);
    line-height: 1;
  }
  .practice-area {
    top: 590px;
    font-size: 62px;
  }
  .phone {
    top: 666px;
    font-size: 60px;
  }
</style>
</head>
<body>
  <main class="wrap-panel">
    <h1 class="brand-name">
      <span class="brand-name__small">THE</span>
      <span class="brand-name__large">HARBOR RIG</span>
    </h1>
    <p class="site-url">THEHARBORRIG.COM</p>
    <p class="tagline">Mobile Law Office - we come to you</p>
    <p class="practice-area">Overtime/Wage and Hour claims</p>
    <p class="phone">1-800-HAR-BOR7</p>
  </main>
</body>
</html>
```